Logo, Business Card & Stationery Design Project

Firstly, we need a quick turnaround for this project.
The company is KTD Financial.
KTD Financial specialises in sourcing, marketing and introducing clients to hassle free investment property opportunities. We are looking for a design representing stability, professionalism and customer focused. We also need to have the feel of being approachable and practical.
The design will be for the logo initially followed by business cards, letterhead (inc word based doc), with compliments, envelopes, stickers and Word documents for a letterhead & title page.
We look forward to seeing your designs.
Target Market(s)
Generally middle class couples aged from 30-50
Industry/Entity Type
Investment
Look and feel
Each slider illustrates characteristics of the customer's brand and the style your logo design should communicate.

```html
<!DOCTYPE html>
<html lang="en">
<head>
<meta charset="utf-8">
<title>KTD Financial – Logo &amp; Stationery</title>
<link href="https://fonts.googleapis.com/css2?family=Questrial&display=swap" rel="stylesheet">
<style>
  :root {
    --brand-blue: #27a7e1;
    --ink: #1f1f1f;
    --grey-text: #7a7a7a;
    --paper: #ffffff;
    --edge: #d6d6d6;
    --ghost: #f1f2f3;
    --shadow: rgba(0,0,0,0.18);
  }
  * { box-sizing: border-box; margin: 0; padding: 0; }
  html, body { width: 1200px; height: 900px; overflow: hidden; background: var(--paper); }
  body { position: relative; font-family: "Questrial", "Century Gothic", sans-serif; color: var(--ink); }

  .wordmark { position: absolute; display: flex; align-items: center; white-space: nowrap; color: var(--ink); line-height: 1; }
  .wordmark .dot { border-radius: 50%; background: var(--brand-blue); flex: none; }
  .wordmark-shadow { position: absolute; border-radius: 50%;
    background: radial-gradient(ellipse at center, var(--shadow) 0%, rgba(0,0,0,0) 70%); }

  /* Primary logo */
  .logo-main { left: 120px; top: 196px; font-size: 68px; letter-spacing: -0.5px; gap: 16px; }
  .logo-main .dot { width: 48px; height: 48px; }
  .logo-main-shadow { left: 110px; top: 266px; width: 230px; height: 30px; }

  /* Business card */
  .business-card { position: absolute; left: 154px; top: 362px; width: 190px; height: 124px;
    background: var(--paper); border: 1px solid var(--edge); overflow: hidden; }
  .business-card .wordmark { left: 10px; top: 16px; font-size: 17px; gap: 6px; }
  .business-card .dot { width: 12px; height: 12px; }
  .card-name { position: absolute; left: 10px; top: 48px; font-size: 13px; }
  .card-role { position: absolute; left: 10px; top: 64px; font-size: 6px; color: var(--grey-text); }
  .card-band { position: absolute; left: 0; bottom: 0; width: 100%; height: 36px; background: var(--brand-blue);
    color: #fff; font-size: 4.5px; display: flex; justify-content: space-between; padding: 10px 10px 0; line-height: 1.7; }

  /* Envelope */
  .envelope { position: absolute; left: 40px; top: 510px; width: 540px; height: 330px;
    background: var(--paper); border: 1px solid var(--edge); overflow: hidden; }
  .envelope-flap { position: absolute; left: 0; top: 0; }
  .flap-text { position: absolute; right: 16px; top: 70px; font-size: 5px; color: #fff; letter-spacing: 0.2px; white-space: nowrap; }
  .envelope .wordmark { left: 30px; top: 138px; font-size: 24px; gap: 8px; }
  .envelope .dot { width: 16px; height: 16px; }
  .envelope-logo-shadow { left: 26px; top: 164px; width: 100px; height: 16px; }
  .ghost-mark { position: absolute; color: var(--ghost); white-space: nowrap; line-height: 1; }
  .envelope .ghost-mark { left: 160px; top: 236px; font-size: 80px; }

  /* Letterhead */
  .letterhead { position: absolute; left: 690px; top: 190px; width: 470px; height: 660px;
    background: var(--paper); border: 1px solid var(--edge); overflow: hidden; }
  .letterhead .wordmark { left: 28px; top: 60px; font-size: 22px; gap: 7px; }
  .letterhead .dot { width: 15px; height: 15px; }
  .letterhead-logo-shadow { left: 26px; top: 84px; width: 90px; height: 14px; }
  .letterhead .ghost-mark { left: 170px; top: 440px; font-size: 120px; }
  .letterhead-contact { position: absolute; left: 28px; top: 562px; font-size: 5.5px; color: var(--grey-text); line-height: 1.6; }
  .letterhead-contact p + p { margin-top: 6px; }
  .letterhead-rule { position: absolute; left: 132px; top: 540px; width: 1px; height: 120px; background: var(--edge); }
</style>
</head>
<body>

  <!-- Primary logo -->
  <div class="wordmark logo-main"><span class="dot"></span>KTD Financial</div>
  <div class="wordmark-shadow logo-main-shadow"></div>

  <!-- Business card -->
  <div class="business-card">
    <div class="wordmark"><span class="dot"></span>KTD Financial</div>
    <div class="card-name">Daniel Hart</div>
    <div class="card-role">Account Manager</div>
    <div class="card-band">
      <div>name@ktdfinancial.com<br>www.ktdfinancial.com</div>
      <div>+44 (0) 200 700 301<br>+44 (0) 200 700 302</div>
    </div>
  </div>

  <!-- Envelope -->
  <div class="envelope">
    <svg class="envelope-flap" width="540" height="86" viewBox="0 0 540 86">
      <path d="M0 86 V40 Q0 6 40 4 Q270 -6 500 4 Q540 6 540 40 V86 Z" fill="var(--brand-blue)"/>
    </svg>
    <div class="flap-text">100 North Road · London · T +44 (0) 200 700 300 · F +44 (0) 200 700 301 · info@ktdfinancial.com · www.ktdfinancial.com</div>
    <div class="wordmark"><span class="dot"></span>KTD Financial</div>
    <div class="wordmark-shadow envelope-logo-shadow"></div>
    <div class="ghost-mark">KTD</div>
  </div>

  <!-- Letterhead -->
  <div class="letterhead">
    <div class="wordmark"><span class="dot"></span>KTD Financial</div>
    <div class="wordmark-shadow letterhead-logo-shadow"></div>
    <div class="ghost-mark">KTD</div>
    <div class="letterhead-contact">
      <p>100 North Road<br>London</p>
      <p>info@ktdfinancial.com<br>www.ktdfinancial.com</p>
      <p>T +44 (0) 200 700 300<br>F +44 (0) 200 700 301</p>
    </div>
    <div class="letterhead-rule"></div>
  </div>

</body>
</html>
```